We need a logo and landing page designed. We are a full-service general contractor based in Tempe Arizona. We can provide all phases of construction from design to completion. We specialize in commercial and residential remodels, as well as ground-up construction. We will like to see designs that primarily used reds, blues, blacks, whites, etc. The design should be a professional yet fun, easy-to-read format. Our name is Oak Ledger Construction...I would like to see some designs that incorporate a "oak ledger" and some without.
The final design should communicate a professional, quality-driven, safety oriented full service business.

Target Market(s)

Building owners, land developers, homeowners

Industry/Entity Type

Commercial Construction

Coding

Coded - Design and coding required

Number of Pages Required

1 page

Font styles to use
Serif

Colors
0054AA
0677BA
7BADD7
CADEEF
E8F1F8
59FF00
82FF00
B8FF75
E3FFCB
F4FFEA
EE7325
F08F49
F5BC92
FAE3D3
FDF4ED
EB3D1F
EC4F4E
F09395
F8D3D4
FCEDEE

```html
<!DOCTYPE html>
<html lang="en">
<head>
<meta charset="utf-8">
<title>Oak Ledger Construction</title>
<link href="https://fonts.googleapis.com/css2?family=Josefin+Sans:wght@400;600;700&display=swap" rel="stylesheet">
<style>
:root{
  --orange:#e04a1c;
  --orange-2:#ee7325;
  --blue:#1b3594;
  --blue-dark:#0f2470;
  --ink:#111111;
  --dark:#333333;
  --text:#333333;
  --white:#ffffff;
  --line:#d9d9d9;
}
*{margin:0;padding:0;box-sizing:border-box}
html,body{width:1200px;height:4598px;overflow:hidden;background:var(--white)}
body{font-family:"Josefin Sans",sans-serif;color:var(--text);position:relative}
.abs{position:absolute}
section{position:absolute;left:0;width:1200px}
.title{font-weight:700;color:var(--ink);text-align:center;letter-spacing:1px}
.btn{position:absolute;display:flex;align-items:center;justify-content:center;color:#fff;font-weight:600;font-size:21px;letter-spacing:.5px;background:linear-gradient(90deg,var(--blue) 0%,var(--blue) 45%,var(--orange) 100%);box-shadow:4px 4px 0 rgba(224,74,28,.35)}
/* Hero */
.hero{top:0;height:700px;overflow:hidden}
.hero-photo{position:absolute;inset:0;background:linear-gradient(100deg,#f4f1ee 0%,#ece3da 38%,#c9a48e 62%,#8c6c5a 80%,#5b4a44 100%)}
.topbar{position:absolute;top:0;left:610px;width:590px;height:46px;background:linear-gradient(90deg,var(--orange) 0%,var(--orange) 40%,var(--blue) 100%);clip-path:polygon(40px 0,100% 0,100% 100%,0 100%)}
.topbar span{position:absolute;top:14px;color:#fff;font-size:16px;display:flex;align-items:center;gap:10px;white-space:nowrap}
.ico-circle{width:26px;height:26px;border:1.5px solid #fff;border-radius:50%;display:inline-flex;align-items:center;justify-content:center}
.logo{position:absolute;left:110px;top:48px;display:flex;align-items:center;gap:10px}
.logo-mark{width:40px;height:40px;background:var(--orange)}
.logo-name{color:var(--orange);font-weight:700;font-size:19px;line-height:20px}
.nav{position:absolute;top:70px;left:0;width:1200px;font-size:17px;color:#111}
.nav a{position:absolute;color:#111;text-decoration:none;white-space:nowrap}
.nav a.active::after{content:"";position:absolute;left:0;right:0;bottom:-9px;height:2px;background:var(--orange)}
.hero h1{position:absolute;left:110px;top:225px;font-size:52px;line-height:62px;font-weight:700;color:#111;letter-spacing:1px;white-space:nowrap}
.hero h1 .first{font-weight:400}
.hero p{position:absolute;left:110px;top:363px;width:580px;font-size:17px;line-height:25px;font-weight:600;color:#111}
.pager{position:absolute;top:644px;left:535px;display:flex;gap:14px}
.pager i{display:block;height:3px;background:var(--orange);width:24px}
.pager i.on{width:44px}
/* About */
.about{top:700px;height:620px}
.about h2{position:absolute;top:75px;width:100%;font-size:31px}
.about .lead{position:absolute;top:125px;left:200px;width:800px;text-align:center;font-size:16.5px;line-height:26px}
.skyline{position:absolute;top:340px;left:0;width:1200px;height:290px;background:linear-gradient(180deg,rgba(230,230,235,0) 0%,rgba(225,228,236,.55) 100%)}
.feature{position:absolute;top:272px;width:320px;height:120px}
.hex{position:absolute;left:0;top:0;width:104px;height:116px;background:var(--orange);clip-path:polygon(50% 0,100% 25%,100% 75%,50% 100%,0 75%,0 25%);display:flex;align-items:center;justify-content:center}
.feature h3{position:absolute;left:116px;top:8px;font-size:17px;font-weight:600;color:#111;letter-spacing:.5px;white-space:nowrap}
.feature p{position:absolute;left:116px;top:35px;width:200px;font-size:12.5px;line-height:17px}
.feature .more{position:absolute;left:116px;top:98px;font-size:13px;font-weight:700;color:#111}
/* Services */
.services-head{top:1320px;height:128px}
.services-head h2{position:absolute;top:50px;width:100%;font-size:30px}
.grid{top:1448px;height:685px}
.cell{position:absolute;width:300px;height:342px}
.cell.dark{background:var(--dark);color:#fff;text-align:center;padding:72px 30px 0}
.cell.orange{background:var(--orange);color:#fff;text-align:center;padding:72px 30px 0}
.cell h3{font-size:21px;font-weight:600;letter-spacing:.5px;margin:0 -20px 18px;white-space:nowrap}
.cell p{font-size:13px;line-height:22px}
.cell .more{display:block;margin-top:14px;font-size:13.5px;font-weight:600}
.photo{position:absolute}
/* Testimonials */
.testi{top:2133px;height:689px}
.testi h2{position:absolute;top:130px;width:100%;font-size:30px}
.face{position:absolute;clip-path:polygon(50% 0,100% 25%,100% 75%,50% 100%,0 75%,0 25%)}
.quote{position:absolute;top:395px;left:245px;width:710px;text-align:center;font-size:18.5px;line-height:26px;color:#111}
.qmark{position:absolute;top:519px;left:570px;width:40px;height:40px;border-radius:50%;background:var(--blue);display:flex;align-items:center;justify-content:center;color:#fff;font-size:34px;font-weight:700;line-height:1;padding-top:14px}
.cite{position:absolute;top:595px;width:100%;text-align:center;font-size:16px;font-weight:600;color:#111}
/* Contact */
.contact{top:2822px;height:588px;overflow:hidden}
.contact-photo{position:absolute;inset:0;background:linear-gradient(120deg,#b7c6d4 0%,#d8cdb9 40%,#c9b26a 65%,#7e7c58 100%)}
.contact-panel{position:absolute;inset:0;background:var(--orange);clip-path:polygon(0 0,510px 0,680px 298px,510px 588px,0 588px)}
.contact h2{position:absolute;left:110px;top:92px;font-size:31px;font-weight:700;color:#fff;letter-spacing:1px}
.field{position:absolute;background:#fff;border-radius:4px;font-size:14px;color:#555;padding:24px 16px 0}
.submit{position:absolute;left:110px;top:443px;width:415px;height:64px;background:var(--blue);border-radius:4px;color:#fff;font-size:21px;font-weight:700;display:flex;align-items:center;justify-content:center;letter-spacing:1px}
/* Specialize */
.special{top:3410px;height:570px}
.special h2{position:absolute;left:110px;top:155px;font-size:32px;font-weight:700;color:#111;letter-spacing:1px}
.special h3{position:absolute;left:110px;top:198px;font-size:21px;font-weight:600;color:#111;letter-spacing:.5px}
.special p{position:absolute;left:110px;width:590px;font-size:14.5px;line-height:26px}
.hex-frame{position:absolute;left:733px;top:68px;width:370px;height:447px}
/* Footer */
.footer{top:3980px;height:618px;background:#000;color:#fff}
.subscribe h2{position:absolute;left:228px;top:187px;font-size:29px;font-weight:700;letter-spacing:1px}
.sub-input{position:absolute;left:597px;top:183px;width:304px;height:44px;background:#fff;color:#333;font-size:13px;padding:16px 20px 0;letter-spacing:1px}
.sub-btn{position:absolute;left:901px;top:183px;width:131px;height:44px;background:var(--blue);color:#fff;font-size:15px;font-weight:700;display:flex;align-items:center;justify-content:center;letter-spacing:1px;border:1px solid #fff}
.rule{position:absolute;left:108px;width:976px;height:1px;background:#555}
.col{position:absolute;top:322px}
.col h4{font-size:20px;font-weight:600;margin-bottom:18px;letter-spacing:.5px;white-space:nowrap}
.col ul{list-style:none}
.col li{font-size:14px;line-height:27px}
.col li::before{content:"→ ";font-size:12px}
.contact-list div{display:flex;gap:10px;font-size:14px;line-height:20px;margin-bottom:14px}
.social{display:flex;gap:18px;margin-top:10px}
.social i{width:26px;height:26px;border-radius:50%;background:var(--blue);display:block}
.copy{position:absolute;left:0;width:1200px;text-align:center;font-size:10px}
</style>
</head>
<body>

<section class="hero">
  <div class="hero-photo" role="img" aria-label="Construction worker in safety vest overlooking a city highway interchange"></div>
  <div class="topbar">
    <span style="left:80px"><i class="ico-circle"><svg width="13" height="13" viewBox="0 0 24 24" fill="#fff"><path d="M6.6 10.8a15 15 0 0 0 6.6 6.6l2.2-2.2c.3-.3.7-.4 1-.2 1.1.4 2.3.6 3.6.6.6 0 1 .4 1 1V20c0 .6-.4 1-1 1C10.6 21 3 13.4 3 4c0-.6.4-1 1-1h3.5c.6 0 1 .4 1 1 0 1.3.2 2.5.6 3.6.1.3 0 .7-.2 1z"/></svg></i>+1 480 555 0142</span>
    <span style="left:272px"><i class="ico-circle"><svg width="13" height="10" viewBox="0 0 24 18" fill="none" stroke="#fff" stroke-width="2"><rect x="1" y="1" width="22" height="16"/><path d="M1 1l11 9 11-9"/></svg></i>info@oakledgerconst.com</span>
  </div>
  <div class="logo"><div class="logo-mark"></div><div class="logo-name">Oak Ledger<br>Construction</div></div>
  <nav class="nav">
    <a class="active" style="left:455px">Home</a>
    <a style="left:573px">About</a>
    <a style="left:693px">Services</a>
    <a style="left:830px">Latest News</a>
    <a style="left:1001px">Contact us</a>
  </nav>
  <h1><span class="first">Welcome to</span><br>Oak Ledger Construction</h1>
  <p>Excepteur sint occaecat cupidatat non proident, sunt in culpa &nbsp;qui officia deserunt mollit anim id est laborum.</p>
  <div class="btn" style="left:110px;top:434px;width:165px;height:56px">Get Started</div>
  <svg class="abs" style="left:0;top:0" width="1200" height="700" viewBox="0 0 1200 700">
    <path d="M0 688 L598 589 L1200 616 L1200 700 L0 700Z" fill="#fff"/>
    <path d="M0 688 L598 589 L598 600 L0 700Z" fill="var(--orange)"/>
    <path d="M598 589 L1200 616 L1200 640 L600 598Z" fill="var(--blue)"/>
  </svg>
  <div class="pager"><i class="on"></i><i></i><i></i></div>
</section>

<section class="about">
  <div class="skyline" aria-hidden="true"></div>
  <h2 class="title">About Oak Ledger Construction</h2>
  <p class="lead">Nemo enim ipsam voluptatem quia voluptas sit aspernatur aut odit aut fugit, sed quia consequuntur magni dolores eos qui ratione voluptatem sequi nesciunt. Neque porro quisquam est, qui dolorem ipsum quia dolor sit amet, consectetur, adipisci velit, sed quia non numquam eius modi tempora incidunt ut labore et dolore magnam aliquam quaerat voluptatem.</p>

  <div class="feature" style="left:110px">
    <div class="hex"><svg width="46" height="46" viewBox="0 0 46 46" fill="#fff"><circle cx="23" cy="12" r="7"/><path d="M11 30c0-7 5-11 12-11s12 4 12 11z"/><path d="M6 38l2 4 4 .5-3 2.5 1 4-4-2-4 2 1-4-3-2.5 4-.5z" transform="translate(3 -8)"/><path d="M6 38l2 4 4 .5-3 2.5 1 4-4-2-4 2 1-4-3-2.5 4-.5z" transform="translate(17 -8)"/><path d="M6 38l2 4 4 .5-3 2.5 1 4-4-2-4 2 1-4-3-2.5 4-.5z" transform="translate(31 -8)"/></svg></div>
    <h3>Experienced Contractor</h3>
    <p>Nemo enim ipsam voltem quia voluptas sit aspernatur aut odit aut fugit.</p>
    <span class="more">Read More &nbsp;→</span>
  </div>
  <div class="feature" style="left:451px">
    <div class="hex"><svg width="46" height="46" viewBox="0 0 46 46" fill="none" stroke="#fff" stroke-width="2.5"><rect x="8" y="14" width="16" height="28"/><rect x="24" y="6" width="14" height="36"/><path d="M12 20h3M17 20h3M12 26h3M17 26h3M12 32h3M17 32h3M28 12h6M28 18h6M28 24h6M28 30h6M4 42h38"/></svg></div>
    <h3>Excellant Service</h3>
    <p>Neque porro quisam est, qui dolorem ipsum quia dolor sit amet, consectetur</p>
    <span class="more">Read More &nbsp;→</span>
  </div>
  <div class="feature" style="left:780px">
    <div class="hex"><svg width="46" height="46" viewBox="0 0 46 46" fill="none" stroke="#fff" stroke-width="2.5"><circle cx="23" cy="19" r="12"/><circle cx="23" cy="19" r="7"/><path d="M16 29l-5 12 5-2 3 4 3-9M30 29l5 12-5-2-3 4-3-9"/></svg></div>
    <h3>High Quality Service</h3>
    <p>Nemo enim ipsam voltem quia voluptas sit aspernatur aut odit aut fugit.</p>
    <span class="more">Read More &nbsp;→</span>
  </div>
  <div class="btn" style="left:519px;top:458px;width:163px;height:58px">Read More</div>
</section>

<section class="services-head">
  <h2 class="title">Our Services</h2>
</section>

<section class="grid">
  <div class="photo" style="left:0;top:0;width:300px;height:342px;background:linear-gradient(135deg,#b9c0c8,#8b8a80 60%,#c6d66a)" role="img" aria-label="Two engineers in hard hats reviewing plans on site"></div>
  <div class="cell dark" style="left:300px;top:0"><h3>Assembly Work</h3><p>Ut enim ad minima veniam, quis nostrum exercitationem ullam corporis suscipit laboriam,consecteur, adipisci velit nisi ut aliquid ex ea commodi consequatur.</p><span class="more">Learn More →</span></div>
  <div class="photo" style="left:600px;top:0;width:300px;height:342px;background:linear-gradient(160deg,#d9c89a,#f1f1ee 50%,#c8c9cc)" role="img" aria-label="Builders in hard hats studying blueprints on a table"></div>
  <div class="cell dark" style="left:900px;top:0"><h3>Heavy Civil Construction</h3><p>Ut enim ad minima veniam, quis nostrum exercitationem ullam corporis suscipit laboriam,consecteur, adipisci velit nisi ut aliquid ex ea commodi consequatur.</p><span class="more">Learn More →</span></div>
  <div class="cell dark" style="left:0;top:342px"><h3>Civil Engineering</h3><p>Quis autem vel eum iure reprehenderit qui in ea voluptate velit esse quam nihil molestiae conseatur, vel illum qui dolorem eum fugiat quo voluptas nulla pariatur.</p><span class="more">Learn More →</span></div>
  <div class="photo" style="left:300px;top:342px;width:300px;height:342px;background:linear-gradient(135deg,#7c8fa0,#c9a48a 50%,#d9673a)" role="img" aria-label="Smiling worker holding a power drill"></div>
  <div class="cell orange" style="left:600px;top:342px"><h3>Building Completion</h3><p>Duis aute irure dolor in reprehenderit in voluptate velit esse cillum dolore eu fugiat nulla pariatur.Excepteur sint occaecat cupidatat non proident, mollit anim id est laborum.</p><span class="more">Learn More →</span></div>
  <div class="photo" style="left:900px;top:342px;width:300px;height:342px;background:linear-gradient(135deg,#3c4a5c,#6f7c86 50%,#d8c64e)" role="img" aria-label="Two workers in hard hats and safety vests on site"></div>
</section>

<section class="testi">
  <h2 class="title">What Customer Says</h2>
  <svg class="abs" style="left:0;top:0" width="1200" height="380">
    <g fill="var(--orange)">
      <polygon points="210,222 262,252 262,312 210,342 158,312 158,252"/>
      <polygon points="393,222 445,252 445,312 393,342 341,312 341,252"/>
      <polygon points="810,222 862,252 862,312 810,342 758,312 758,252"/>
      <polygon points="993,222 1045,252 1045,312 993,342 941,312 941,252"/>
    </g>
    <polygon points="600,191 677,236 677,325 600,370 523,325 523,236" fill="var(--blue)"/>
  </svg>
  <div class="face" style="left:162px;top:226px;width:96px;height:112px;background:linear-gradient(135deg,#e2c4b4,#b58a78)" role="img" aria-label="Customer portrait"></div>
  <div class="face" style="left:345px;top:226px;width:96px;height:112px;background:linear-gradient(135deg,#c7ccd2,#8e7a6c)" role="img" aria-label="Customer portrait"></div>
  <div class="face" style="left:530px;top:198px;width:140px;height:164px;background:linear-gradient(135deg,#f3d9c6,#7d5b4a)" role="img" aria-label="Featured customer portrait"></div>
  <div class="face" style="left:762px;top:226px;width:96px;height:112px;background:linear-gradient(135deg,#d9b39c,#8a4c3a)" role="img" aria-label="Customer portrait"></div>
  <div class="face" style="left:945px;top:226px;width:96px;height:112px;background:linear-gradient(135deg,#d6d2cc,#7b746c)" role="img" aria-label="Customer portrait"></div>
  <p class="quote">"Itaque earum rerum hic tenetur a sapiente delectus, ut aut reiciendis voluptatibus maiores alias consequatur aut perferendis doloribus asperiores repellat!Excepteur sint occaecat cupidatat non proident, sunt in culpa qui officia deserunt mollit anim id est laborum."</p>
  <div class="qmark">”</div>
  <p class="cite">Dana Whitfield &nbsp;&nbsp;- &nbsp;&nbsp;Thank You Oak Ledger Construction</p>
</section>

<section class="contact">
  <div class="contact-photo" role="img" aria-label="Engineers in hard hats pointing across a construction site with a crane"></div>
  <div class="contact-panel"></div>
  <h2>Get In Touch</h2>
  <div class="field" style="left:110px;top:168px;width:196px;height:64px">Full Name</div>
  <div class="field" style="left:326px;top:168px;width:196px;height:64px">Email</div>
  <div class="field" style="left:110px;top:243px;width:415px;height:64px">Phone no</div>
  <div class="field" style="left:110px;top:316px;width:415px;height:110px">Message</div>
  <div class="submit">SUBMIT</div>
</section>

<section class="special">
  <h2>We Specialize In</h2>
  <h3>Residential Oak Ledger Remodels</h3>
  <p style="top:238px">Nemo enim ipsam voluptatem quia voluptas sit aspernatur aut odit aut fugit, sed quia consequuntur magni dolores eos qui ratione voluptatem sequi nesciunt. Neque porro quisquam est, qui dolorem ipsum quia dolor sit amet, consectetur, adipisci velit, sed quia non numquam eius modi tempora incidunt ut labore et dolore magnam aliquam quaerat voluptatem.</p>
  <p style="top:392px">Ut enim ad minima veniam, quis nostrum exercitationem ullam corporis suscipit laboriosam, nisi ut aliquid ex ea commodi consequatur.</p>
  <div class="btn" style="left:112px;top:455px;width:163px;height:60px">Learn More</div>
  <svg class="hex-frame" viewBox="0 0 370 447">
    <polygon points="185,0 370,100 185,200 0,100" fill="var(--orange)"/>
    <polygon points="185,447 370,347 185,247 0,347" fill="var(--blue)"/>
  </svg>
  <div class="face" style="left:733px;top:90px;width:370px;height:403px;background:linear-gradient(180deg,#e7a27e 0%,#b77d8f 35%,#9a6b6a 55%,#6d84b8 80%,#3d4f8c 100%)" role="img" aria-label="Waterfront apartment buildings below a hillside at sunset"></div>
</section>

<section class="footer">
  <svg class="abs" style="left:0;top:0" width="1200" height="110">
    <path d="M0 0 L1200 0 L1200 6 L600 102 L0 6Z" fill="#fff"/>
    <path d="M0 6 L600 102 L600 110 L0 16Z" fill="var(--orange)"/>
    <path d="M600 102 L1200 6 L1200 14 L600 110Z" fill="var(--blue)"/>
  </svg>
  <div class="subscribe"><h2>Subscribe for Join us</h2></div>
  <div class="sub-input">Enter Your Email</div>
  <div class="sub-btn">SUBSCRIBE</div>
  <div class="rule" style="top:275px"></div>

  <div class="col contact-list" style="left:108px">
    <h4>Contact</h4>
    <div><svg width="12" height="16" viewBox="0 0 12 16" fill="#fff"><path d="M6 0a6 6 0 0 0-6 6c0 4.5 6 10 6 10s6-5.5 6-10a6 6 0 0 0-6-6zm0 8.5A2.5 2.5 0 1 1 6 3.5a2.5 2.5 0 0 1 0 5z"/></svg><span>12 Mesa Verde Lane<br>Tempe, Arizona</span></div>
    <div><svg width="13" height="13" viewBox="0 0 24 24" fill="#fff"><path d="M6.6 10.8a15 15 0 0 0 6.6 6.6l2.2-2.2c.3-.3.7-.4 1-.2 1.1.4 2.3.6 3.6.6.6 0 1 .4 1 1V20c0 .6-.4 1-1 1C10.6 21 3 13.4 3 4c0-.6.4-1 1-1h3.5c.6 0 1 .4 1 1 0 1.3.2 2.5.6 3.6.1.3 0 .7-.2 1z"/></svg><span>+1 480 555 0142</span></div>
    <div style="margin-top:10px"><svg width="13" height="10" viewBox="0 0 24 18" fill="#fff"><rect width="24" height="18"/></svg><span>info@oakledgerconstr.com</span></div>
  </div>
  <div class="col" style="left:397px">
    <h4>Quick Links</h4>
    <ul><li>Home</li><li>About</li><li>Services</li><li>Testimonials</li><li>Contact</li></ul>
  </div>
  <div class="col" style="left:613px">
    <h4>Help Center</h4>
    <ul><li>FAQ</li><li>Terms</li><li>Privacy Policy</li><li>Support Center</li><li>Conditions</li></ul>
  </div>
  <div class="col" style="left:818px;width:280px">
    <h4>About Oak Ledger Contractor</h4>
    <p style="font-size:13px;line-height:20px;width:210px">Excepteur sint occaecat cupidatat non proident, sunt in culpa qui officia deserunt mollit</p>
    <p style="font-size:10px;font-weight:700;margin-top:6px;letter-spacing:.5px">FOLLOW US ON:</p>
    <div class="social"><i></i><i></i><i></i><i></i></div>
  </div>
  <div class="rule" style="top:543px;left:108px;width:340px"></div>
  <div class="rule" style="top:543px;left:742px;width:342px"></div>
</section>
<p class="copy" style="color:#fff;top:4519px">Copyrights@2022.oakledgerconst All Rights Reserved</p>

</body>
</html>
```